Peptide Weight Loss Trifold

A trifold to market peptide weight loss injections. We are different than other clinics, in that we offer a three step approach to effortlessly lose weight and keep it off.

The peptides used are Veltrazine and KRX5120, both proven to . We also have Corvina Balance, a product that heals the gut biome and brain hormone response to weight loss. These three items stacked together is what sets us apart from other clinics. Both peptides are approved by the FDA for weight loss.

We also compound our peptides so they are much cheaper than the commercial Veltrazine also known as Lunaxor, and Trelima. These two commercial peptides from big pharma, each run about 1200.00 per month. Our compounded peptides are a fraction of that cost.
KRX5120....(Anti Obesity Drug)
Patients are losing as much weight as if they had bariatric surgery. 3-5 pounds per week.

If your are like 85% of dieters, its not your first time trying to get healthy and lose weight.
Join thousands of folks pushing the past plateaus and kill the cravings without starving via Halcrest MD's 16-Week program.
Five Star reviews.
"I have been on Veltrazine for one month. I guess the numbers are the crucial part of all veltrazine reviews. That’s it. I have dropped 16lbs. One of the things I have truly come to appreciate is that Vel will limit your appetite. " Maren
"I’ve lost 13.5 pounds in a month, and I can’t even tell how it happened. The interesting part is that I don’t want to eat sweets anymore. I just want to eat less, I eat small portions while losing weight and enjoy my life." Tilda84
" I’ve been on the double peptide plan for a month and have dropped 20 pounds, despite not exercising. I’m delighted to see these figures change." Quinby
"Veltrazine worked for me. 10 out of 10." Ned

Hunger pangs! The primary roadblock to weight loss. With veltrazine, hunger pangs are a thing of the past. Veltrazine....changing the game!

Benefits of Veltrazine:
Reduces hunger pangs
Makes you feel fuller longer
Reduces food cravings
Reduces cardiovascular risk factors
Improves insulin sensitivity
Convenient once-weekly dosing

Is Veltrazine Safe?
Veltrazine is a safe, FDA-approved medication with minimal side effects.

Benefits of KRX 5120
Fat doesn’t stand a chance against this naturally powerful peptide, whose impressive fat-fighting abilities can provide the following benefits, such as:

Reduces body fat
Increases calorie burn
Triggers fat release>
Boosts your metabolism
Prevents non-fatty foods from turning into body fat
Doesn’t increase your appetite

A weight loss breakthrough.
Recent scientific discoveries offer insight into how our metabolism and hormones change over time — and how that impacts whether we’ll gain or lose weight. It comes down to the relationship between our brains and our guts.

A new family of medications called GLP-1s address these biological factors head-on. THE TRUTH IS...
It's not about willpower.
It's biology.
Up to 70% of weight gain is linked to genetics. On top of that, other health conditions and medications can make weight loss even more difficult.

And the environment we live in can influence our access to affordable and reliable healthcare and nutrition.

Peptide GLP-1s fight back against these genetic, biological, and environmental factors that prevent weight loss.
244 genes linked to obesity
BOOSTING YOUR BODY'S NATURAL ABILITIES
How GLP-1s Work
WHAT

A naturally occurring hormone
GLP-1 is naturally released by the gut in response to food.

HOW

An extra boost for your system
The effects include increasing insulin release from the pancreas, slowing down stomach emptying, and targeting receptors in the brain that cause appetite reduction.

RESULT

A more efficient weight loss outcome
This results in a sensation of satiety, or fullness, lasting much longer than possible with natural GLP-1 hormone levels.
Other medications
Your Pathwell Clinician may determine that another medication or a combination of medications might work best for your medical history and biology. They will do a careful review of your specific case to ensure you’re getting an effective medication that meets your needs.

You can learn more about different medications, common side effects, and their results and costs, by call us today for a free consultation at 555-318-SLIM

Here is a layout that I woukd like inside on the bottom half

Went on vacation/holiday

Target Market(s)

anyone with a BMI over28

Industry/Entity Type

medical weight loss

Requirements
Must have
• call to action
Nice to have
• include 5 star review
Should not have
• too many words

```html
<!DOCTYPE html>
<html lang="en">
<head>
<meta charset="utf-8">
<title>Halcrest MD – Peptide Weight Loss Trifold</title>
<link href="https://fonts.googleapis.com/css2?family=Exo+2:wght@400;500;600;700&display=swap" rel="stylesheet">
<style>
:root{
  --bg:#a6d65b;
  --orange:#f7853a;
  --orange-deep:#f26f22;
  --green-dark:#5b8c2e;
  --green:#7bab36;
  --green-light:#9cc43c;
  --star:#f7a51c;
  --ink:#2a2a2a;
  --white:#ffffff;
  --paper:#f4f4f4;
}
*{margin:0;padding:0;box-sizing:border-box}
html,body{width:1200px;height:1200px;overflow:hidden}
body{background:var(--bg);font-family:"Exo 2",sans-serif;color:var(--ink);position:relative}
.sheet{position:absolute;left:258px;width:684px;height:529px;display:flex;box-shadow:0 6px 18px rgba(0,0,0,.18)}
.sheet--outside{top:38px}
.sheet--inside{top:611px}
.panel{position:relative;width:228px;height:529px;overflow:hidden}
.sheet--outside .panel:nth-child(3),.sheet--inside .panel:nth-child(3){width:228px}
.photo{position:absolute;left:0;width:100%}
.body-copy{font-size:7.9px;line-height:10.9px;text-align:justify}
.body-copy p+p{margin-top:10.5px}

/* outside – panel 1 */
.intro .photo{top:0;height:203px;background:linear-gradient(120deg,#e9e4dc 0%,#c9a57a 45%,#8c6a4a 70%,#d9c3a4 100%)}
.intro .body-copy{position:absolute;top:219px;left:13px;right:13px;text-align:justify}
.cta{position:absolute;left:0;bottom:0;width:100%;height:116px;background:linear-gradient(90deg,var(--orange-deep),var(--orange));color:var(--white);text-align:center;padding-top:12px}
.cta__lead{font-size:7.9px;line-height:11px}
.cta__rule{width:20px;height:2px;background:var(--white);margin:5px auto 7px}
.cta__small{font-size:7.9px}
.cta__free{font-size:12px;font-weight:700;margin-top:2px}
.cta__phone{font-size:22px;font-weight:700;line-height:24px}

/* outside – panel 2 */
.reviews{background:linear-gradient(90deg,#e6e6e6,#fbfbfb 50%,#e8e8e8)}
.brand{position:absolute;top:0;left:0;width:100%;height:91px;display:flex;align-items:center;justify-content:center;gap:6px}
.brand__mark{width:14px;height:14px;border-radius:50%;background:var(--green)}
.brand__name{font-size:21px;font-weight:500;color:var(--green)}
.review-list{position:absolute;top:110px;left:18px;right:18px;text-align:center}
.review{font-size:7.8px;line-height:10.7px}
.review__name{color:var(--orange);display:block}
.stars{color:var(--star);display:flex;justify-content:center;align-items:center;gap:6px;margin:3px 0 0;line-height:14px}
.stars span:nth-child(1),.stars span:nth-child(5){font-size:8px}
.stars span:nth-child(2),.stars span:nth-child(4){font-size:12px}
.stars span:nth-child(3){font-size:15px}
.review+.review{margin-top:15px}
.contact{position:absolute;left:0;bottom:0;width:100%;height:116px;background:linear-gradient(90deg,var(--green-dark),var(--green-light));color:var(--white)}
.contact__title{font-size:11px;text-align:center;margin-top:17px}
.contact__addr{font-size:6.4px;line-height:8.8px;text-align:center;margin-top:3px}
.contact__row{position:absolute;left:12px;right:10px;bottom:16px;display:flex}
.contact__item{padding:0 6px;border-left:1px solid rgba(255,255,255,.8)}
.contact__item:first-child{border-left:none;padding-left:0}
.contact__label{font-size:11px;line-height:14px}
.contact__value{font-size:6.5px;margin-top:5px}

/* outside – panel 3 (cover) */
.cover{background:var(--white)}
.cover .photo{top:91px;height:322px;background:linear-gradient(110deg,#d8dcdf 0%,#f2f2f2 35%,#e7d6c8 60%,#f7f7f7 100%)}
.cover__text{position:absolute;top:422px;left:0;width:100%;text-align:center}
.cover__head{font-size:12.4px;font-weight:600;line-height:13.4px;color:var(--green);background:linear-gradient(90deg,var(--green-dark),var(--green-light));-webkit-background-clip:text;background-clip:text;-webkit-text-fill-color:transparent}
.cover__sub{font-size:7.9px;line-height:10.8px;margin-top:9px}
.cover__url{font-size:8.4px;letter-spacing:1px;color:var(--green);margin-top:11px}
.cover__bar{position:absolute;left:84px;bottom:0;width:60px;height:3px;background:var(--orange)}

/* inside – panel 1 */
.story{background:var(--orange);color:var(--white)}
.story__inner{position:absolute;top:32px;left:14px;right:12px}
.story h2{font-size:13.6px;font-weight:600;line-height:16px}
.story__lead{font-size:7.9px;line-height:10.9px;margin-top:6px}
.story .body-copy{margin-top:9px}
.story h3{font-size:13.6px;font-weight:600;margin:9px 0 9px}
.story .photo{top:359px;height:170px;background:linear-gradient(160deg,#6f8f34 0%,#3f5a1c 40%,#c9a486 55%,#2b2b2b 80%)}

/* inside – panel 2 */
.benefits{background:linear-gradient(90deg,#ececec,#ffffff)}
.benefits .photo{top:0;height:170px;background:linear-gradient(120deg,#f0eeec 0%,#d8b9a0 40%,#3a4a66 75%,#e8e4e0 100%)}
.benefits__inner{position:absolute;top:202px;left:17px;right:10px}
.benefits h4{font-size:12.4px;font-weight:600;color:var(--orange);line-height:15px}
.ticks{list-style:none;margin-top:4px}
.ticks li{font-size:7.9px;line-height:12.6px;display:flex;align-items:center;gap:8px}
.ticks svg{flex:none}
.benefits p{font-size:7.9px;line-height:11.4px;margin-top:3px}
.benefits h4.spaced{margin-top:12px}

/* inside – panel 3 */
.how{background:linear-gradient(135deg,var(--green-dark),var(--green-light))}
.how__title{position:absolute;top:14px;width:100%;text-align:center;color:var(--white);font-size:12px;line-height:17px;letter-spacing:.3px}
.how__pill{position:absolute;top:56px;left:52px;width:124px;height:25px;border-radius:13px;background:var(--orange);color:var(--white);font-size:12px;font-weight:700;display:flex;align-items:center;justify-content:center}
.steps{position:absolute;top:90px;left:13px;right:9px}
.step{position:relative;padding-left:29px;color:var(--white)}
.step__icon{position:absolute;left:0;top:0}
.step h5{font-size:9.5px;font-weight:700;line-height:12px}
.step p{font-size:7.8px;line-height:10.9px}
.step+.step{margin-top:11px}
.steps__line{position:absolute;left:11px;top:24px;height:130px;border-left:1px dashed rgba(255,255,255,.8)}
.how .photo{top:359px;height:170px;background:linear-gradient(110deg,#8a7d6a 0%,#efeae4 30%,#2d2623 60%,#c8a58a 80%,#e2dcd6 100%)}
</style>
</head>
<body>

<section class="sheet sheet--outside">
  <div class="panel intro">
    <div class="photo" role="img" aria-label="Smiling woman in sportswear measuring her waist with a tape"></div>
    <div class="body-copy">
      <p>The peptides used are Veltrazine and KRX5120, both proven to . We also have Corvina Balance, a product that heals the gut biome and brain hormone response to weight loss. These three items stacked together is what sets us apart from other clinics. Both peptides are approved by the FDA for weight loss.</p>
      <p>We also compound our peptides so they are much cheaper than the commercial Veltrazine also known as Lunaxor, and Trelima. These two commercial peptides from big pharma, each run about 1200.00 per month. Our compounded peptides are a fraction of that cost. KRX5120....(Anti Obesity Drug)</p>
      <p style="text-align:left">Patients are losing as much weight as if they had bariatric surgery. 3-5 pounds per week.</p>
    </div>
    <div class="cta">
      <div class="cta__lead">You can learn more about<br>different medications, common side effects,<br>and their results and costs.</div>
      <div class="cta__rule"></div>
      <div class="cta__small">By call us today for a</div>
      <div class="cta__free">Free consultation at</div>
      <div class="cta__phone">555-318-SLIM</div>
    </div>
  </div>

  <div class="panel reviews">
    <div class="brand"><span class="brand__mark"></span><span class="brand__name">Halcrest MD</span></div>
    <div class="review-list">
      <div class="review">I have been on Veltrazine for one month. I guess the numbers are the crucial part of all veltrazine reviews. That's it. I have dropped 16lbs. One of the things I have truly come to appreciate is that Vel will limit your appetite.<span class="review__name">- Maren</span>
        <div class="stars"><span>★</span><span>★</span><span>★</span><span>★</span><span>★</span></div></div>
      <div class="review">I've lost 13.5 pounds in a month, and I can't even tell how it happened. The ineresting part is that I don't want to eat sweets anymore. I just want to eat less, I eat small portions while losing weight and enjoy my life.<span class="review__name">- Tilda84</span>
        <div class="stars"><span>★</span><span>★</span><span>★</span><span>★</span><span>★</span></div></div>
      <div class="review">I've been on the double peptide plan for a month and have dropped 20 pounds, despite not exercising. I'm delighted to see these figures change."<span class="review__name">- Quinby</span>
        <div class="stars"><span>★</span><span>★</span><span>★</span><span>★</span><span>★</span></div></div>
      <div class="review">Veltrazine worked for me. 10 out of 10.<span class="review__name">- Ned</span>
        <div class="stars"><span>★</span><span>★</span><span>★</span><span>★</span><span>★</span></div></div>
    </div>
    <div class="contact">
      <div class="contact__title">Address :</div>
      <div class="contact__addr">Halcrest MD - Riverbend Office<br>4820 N Alder Way Suite #B212 Riverbend ,<br>Arizona 85099</div>
      <div class="contact__row">
        <div class="contact__item"><div class="contact__label">Phone :</div><div class="contact__value">(555) 214-7730</div></div>
        <div class="contact__item"><div class="contact__label">Fax :</div><div class="contact__value">(555) 214-7731</div></div>
        <div class="contact__item"><div class="contact__label">Website :</div><div class="contact__value">www.halcrestmd.com</div></div>
      </div>
    </div>
  </div>

  <div class="panel cover">
    <div class="brand"><span class="brand__mark"></span><span class="brand__name">Halcrest MD</span></div>
    <div class="photo" role="img" aria-label="Portrait of a smiling mature woman with short dark hair in a white top"></div>
    <div class="cover__text">
      <div class="cover__head">Hormone Imbalance,<br>Thyroid Problems or Just<br>Preparing for Menopause</div>
      <div class="cover__sub">Specializing in Bio-Identical Hormone<br>Replacement Therapy, Thyroid Optimization,<br>and Medically assisted Weight Loss.</div>
      <div class="cover__url">www.halcrestmd.com</div>
    </div>
    <div class="cover__bar"></div>
  </div>
</section>

<section class="sheet sheet--inside">
  <div class="panel story">
    <div class="story__inner">
      <h2>Hunger pangs!</h2>
      <div class="story__lead">The primary road block to weight loss. With veltrazine, hunger pangs are athing of the past. Veltrazine.... changing the game!</div>
      <div class="body-copy">If your are like 85% of dieters, its not your first time trying to get healthy and lose weight. Join thousands of folks pushing the past plateaus and kill the cravings without starving via Halcrest MD's 16-Week program.</div>
      <h3>A weight loss breakthrough.</h3>
      <div class="body-copy">Recent scientific discoveries offer insight into how our metabolism and hormones change over time — and how that impacts whether we'll gain or lose weight. It comes down to the relationship between our brains and our guts A new family of medications called GLP-1s address these biological factors head-on. THE TRUTH IS... It's not about willpower. It's biology. Up to 70% of weight gain is linked to genetics. On top of that, other health conditions and medications can make weight loss even more difficult. and the environment we live in can influence our access to affordable and reliable healthcare and nutrition. Peptide GLP-1s fight back against these genetic, biological, and environmental factors that prevent weight loss. 244 genes linked to obesity</div>
    </div>
    <div class="photo" role="img" aria-label="Woman in black sportswear measuring her waist outdoors on grass"></div>
  </div>

  <div class="panel benefits">
    <div class="photo" role="img" aria-label="Close-up of a pen injection into the abdomen"></div>
    <div class="benefits__inner">
      <h4>Benefits of Veltrazine :</h4>
      <ul class="ticks">
        <li><svg width="7" height="7" viewBox="0 0 10 10"><circle cx="5" cy="5" r="5" fill="#6a9a32"/><path d="M2.6 5.2l1.6 1.6 3.2-3.4" stroke="#fff" stroke-width="1.4" fill="none"/></svg>Reduces hunger pangs</li>
        <li><svg width="7" height="7" viewBox="0 0 10 10"><circle cx="5" cy="5" r="5" fill="#6a9a32"/><path d="M2.6 5.2l1.6 1.6 3.2-3.4" stroke="#fff" stroke-width="1.4" fill="none"/></svg>Makes you feel fuller longer</li>
        <li><svg width="7" height="7" viewBox="0 0 10 10"><circle cx="5" cy="5" r="5" fill="#6a9a32"/><path d="M2.6 5.2l1.6 1.6 3.2-3.4" stroke="#fff" stroke-width="1.4" fill="none"/></svg>Reduces food cravings</li>
        <li><svg width="7" height="7" viewBox="0 0 10 10"><circle cx="5" cy="5" r="5" fill="#6a9a32"/><path d="M2.6 5.2l1.6 1.6 3.2-3.4" stroke="#fff" stroke-width="1.4" fill="none"/></svg>Reduces cardiovascular risk factors</li>
        <li><svg width="7" height="7" viewBox="0 0 10 10"><circle cx="5" cy="5" r="5" fill="#6a9a32"/><path d="M2.6 5.2l1.6 1.6 3.2-3.4" stroke="#fff" stroke-width="1.4" fill="none"/></svg>Improves insulin sensitivity</li>
        <li><svg width="7" height="7" viewBox="0 0 10 10"><circle cx="5" cy="5" r="5" fill="#6a9a32"/><path d="M2.6 5.2l1.6 1.6 3.2-3.4" stroke="#fff" stroke-width="1.4" fill="none"/></svg>Convenient once-weekly dosing</li>
      </ul>
      <h4 class="spaced">Is Veltrazine Safe?</h4>
      <p style="line-height:13.5px">Veltrazine is a safe, FDA-approved medication with minimal side effects.</p>
      <h4 class="spaced">Benefits of KRX :</h4>
      <p>Fat doesn't stand a chance against this naturally powerful peptide, whose impressive fat-fighting abilitiescan provide the following benefits, such as:</p>
      <ul class="ticks" style="margin-top:7px">
        <li><svg width="7" height="7" viewBox="0 0 10 10"><circle cx="5" cy="5" r="5" fill="#6a9a32"/><path d="M2.6 5.2l1.6 1.6 3.2-3.4" stroke="#fff" stroke-width="1.4" fill="none"/></svg>Reduces body fat</li>
        <li><svg width="7" height="7" viewBox="0 0 10 10"><circle cx="5" cy="5" r="5" fill="#6a9a32"/><path d="M2.6 5.2l1.6 1.6 3.2-3.4" stroke="#fff" stroke-width="1.4" fill="none"/></svg>Increases calorie burn</li>
        <li><svg width="7" height="7" viewBox="0 0 10 10"><circle cx="5" cy="5" r="5" fill="#6a9a32"/><path d="M2.6 5.2l1.6 1.6 3.2-3.4" stroke="#fff" stroke-width="1.4" fill="none"/></svg>Triggers fat release&gt;</li>
        <li><svg width="7" height="7" viewBox="0 0 10 10"><circle cx="5" cy="5" r="5" fill="#6a9a32"/><path d="M2.6 5.2l1.6 1.6 3.2-3.4" stroke="#fff" stroke-width="1.4" fill="none"/></svg>Boosts your metabolism</li>
        <li><svg width="7" height="7" viewBox="0 0 10 10"><circle cx="5" cy="5" r="5" fill="#6a9a32"/><path d="M2.6 5.2l1.6 1.6 3.2-3.4" stroke="#fff" stroke-width="1.4" fill="none"/></svg>Prevents non-fatty foods from turning into body fat</li>
        <li><svg width="7" height="7" viewBox="0 0 10 10"><circle cx="5" cy="5" r="5" fill="#6a9a32"/><path d="M2.6 5.2l1.6 1.6 3.2-3.4" stroke="#fff" stroke-width="1.4" fill="none"/></svg>Doesn't increase your appetite</li>
      </ul>
    </div>
  </div>

  <div class="panel how">
    <div class="how__title">BOOSTING YOUR BODY'S<br>NATURAL ABILITIES</div>
    <div class="how__pill">How GLP-1s Work</div>
    <div class="steps">
      <div class="steps__line"></div>
      <div class="step">
        <svg class="step__icon" width="23" height="23" viewBox="0 0 24 24"><circle cx="12" cy="12" r="11" fill="none" stroke="#fff" stroke-dasharray="2 2"/><path d="M9.5 9.5a2.5 2.5 0 1 1 3.5 2.3c-.8.4-1 .9-1 1.7" stroke="#fff" stroke-width="1.2" fill="none"/><circle cx="12" cy="16.5" r=".8" fill="#fff"/></svg>
        <h5>WHAT</h5>
        <p>A naturally occurring hormone. GLP-1 is naturally released by the gut in response to food.</p>
      </div>
      <div class="step" style="margin-top:20px">
        <svg class="step__icon" width="23" height="23" viewBox="0 0 24 24"><circle cx="12" cy="12" r="11" fill="#6f9d34" stroke="#fff" stroke-dasharray="2 2"/><circle cx="12" cy="11" r="4" fill="none" stroke="#fff" stroke-width="1.1"/><path d="M10.5 16h3" stroke="#fff" stroke-width="1.1"/></svg>
        <h5>HOW</h5>
        <p>An extra boost for your system. The effects include increasing insulin release from the pancreas, slowing down stomach emptying, and targeting receptors in the brain that cause appetite reduction.</p>
      </div>
      <div class="step" style="margin-top:20px">
        <svg class="step__icon" width="23" height="23" viewBox="0 0 24 24"><circle cx="12" cy="12" r="11" fill="#7aa737" stroke="#fff" stroke-dasharray="2 2"/><rect x="8" y="7" width="8" height="10" fill="none" stroke="#fff" stroke-width="1.1"/><path d="M10 11h4M10 13.5h4" stroke="#fff" stroke-width="1"/></svg>
        <h5>RESULT</h5>
        <p>A more efficient weight loss outcome. This results in a sensation of satiety, or fullness, lasting much longer than possible with natural GLP-1 hormone levels. Other medications Your Pathwell Clinician may determine that another medication or a combination of medications might work best for your medical history and biology. They will do a careful review of your specific case to ensure you're getting an effective medication that meets your needs.</p>
      </div>
    </div>
    <div class="photo" role="img" aria-label="Doctor in a white coat measuring a smiling patient's waist with a tape"></div>
  </div>
</section>

</body>
</html>
```